Brisk Nook needs a packaging design

Hello!

I need an eye-catching package design for Brisk Nook mobile accessories. The products inside the box package include a bluetooth speaker and a power bank.

This is under our brandname called Brisk Nook. The text should be in the picture, no matter how the design looks.

I have attached pictures of the products. If you think that there will not be well with the images it is ok. Then these texts be included:
Bluetooth Speaker
Power Bank

This is our slogan:
Music + Power. It's your imagination that sets the limits!

The image will be printed on a carton pack containing with four color printing. Customising the picture for the type of print.

Should be in 300 DPI High resolution.

Please check the attached pictures where your design will be printed.
Also, I attached design inspiration images for reference. Feel free to do something similar like that.

For the size and dimensions please refer to this attachment:

So remember, the important thing is the design. Do your absolute best!
Updates

Reason: Hello everyone! I would like to see a design without the images of the accessories. Only text. I also dont want the text "Its you imagination that sets...". Thank you!

Target Market(s)

Mobile accessories

Industry/Entity Type

Electronics

Requirements
Must have
• This text:
• Brisk Nook
Nice to have
• Music + Power.

```html
<!DOCTYPE html>
<html lang="en">
<head>
<meta charset="utf-8">
<title>Brisk Nook – Packaging Front</title>
<link href="https://fonts.googleapis.com/css2?family=Audiowide&display=swap" rel="stylesheet">
<style>
  :root {
    --magenta: #d2306f;
    --pink: #f06fb4;
    --violet: #b06ad8;
    --sky: #27b8f2;
    --ice: #dff1ff;
    --crimson: #b0103e;
    --ink: #2a0a1c;
    --white: #ffffff;
  }
  html, body {
    margin: 0;
    padding: 0;
    width: 1200px;
    height: 1200px;
    overflow: hidden;
  }
  .package-front {
    position: relative;
    width: 1200px;
    height: 1200px;
    overflow: hidden;
    background:
      linear-gradient(180deg, rgba(255,255,255,0) 0%, rgba(255,255,255,0.35) 30%, rgba(255,255,255,0.15) 50%, rgba(240,60,150,0.35) 75%, rgba(200,20,90,0.55) 100%),
      linear-gradient(90deg, var(--magenta) 0%, var(--pink) 22%, var(--violet) 45%, var(--sky) 78%, var(--sky) 100%);
  }
  .stripe-layer {
    position: absolute;
    inset: 0;
    background: repeating-linear-gradient(180deg,
      rgba(255,255,255,0.16) 0 38px,
      rgba(255,255,255,0) 38px 70px,
      rgba(60,40,140,0.08) 70px 96px,
      rgba(255,255,255,0) 96px 130px);
  }
  .glow-center {
    position: absolute;
    left: 250px;
    top: 60px;
    width: 760px;
    height: 560px;
    border-radius: 50%;
    background: radial-gradient(closest-side, rgba(240,248,255,0.75), rgba(240,248,255,0));
  }
  .title-band {
    position: absolute;
    left: 0;
    top: 398px;
    width: 1145px;
    height: 86px;
    background: linear-gradient(90deg, rgba(150,210,255,0.25), rgba(150,210,255,0.75) 40%, rgba(120,200,250,0.7));
  }
  .mid-band {
    position: absolute;
    left: 0;
    top: 560px;
    width: 1200px;
    height: 70px;
    background: linear-gradient(90deg, rgba(255,110,170,0.3), rgba(90,170,240,0.55) 50%, rgba(110,120,220,0.5));
  }
  .low-band {
    position: absolute;
    left: 0;
    top: 662px;
    width: 1200px;
    height: 34px;
    background: linear-gradient(90deg, rgba(190,60,110,0.3), rgba(240,140,140,0.55) 50%, rgba(150,100,190,0.45));
  }
  .brand-name {
    position: absolute;
    left: 0;
    width: 1200px;
    top: 386px;
    margin: 0;
    text-align: center;
    padding-right: 5px;
    box-sizing: border-box;
    font-family: "Audiowide", sans-serif;
    font-weight: 400;
    font-size: 96px;
    letter-spacing: 6px;
    color: var(--white);
    text-shadow: 4px 5px 0 rgba(80,30,90,0.35);
    white-space: nowrap;
  }
  .speaker-art {
    position: absolute;
    left: 0;
    top: 520px;
    width: 880px;
    height: 680px;
  }
  .slogan-band {
    position: absolute;
    left: 680px;
    top: 902px;
    width: 520px;
    height: 82px;
    background: linear-gradient(90deg, rgba(42,10,28,0.85), rgba(90,15,50,0.7));
  }
  .slogan {
    position: absolute;
    left: 695px;
    top: 914px;
    margin: 0;
    font-family: "Audiowide", sans-serif;
    font-size: 44px;
    color: var(--white);
    letter-spacing: 1px;
    white-space: nowrap;
  }
  .bottom-wash {
    position: absolute;
    left: 0;
    bottom: 0;
    width: 1200px;
    height: 260px;
    background: linear-gradient(180deg, rgba(220,30,100,0), rgba(220,30,100,0.45));
  }
</style>
</head>
<body>
  <main class="package-front">
    <div class="stripe-layer"></div>
    <div class="glow-center"></div>
    <div class="mid-band"></div>
    <div class="low-band"></div>
    <div class="bottom-wash"></div>
    <div class="title-band"></div>
    <h1 class="brand-name">BRISK NOOK</h1>

    <svg class="speaker-art" viewBox="0 0 880 680" role="img" aria-label="Illustration of glossy red loudspeaker cones with sparkles">
      <defs>
        <radialGradient id="speakerWash" cx="40%" cy="62%" r="62%">
          <stop offset="0%" stop-color="#c0143f"/>
          <stop offset="45%" stop-color="#9e0f3c" stop-opacity="0.9"/>
          <stop offset="80%" stop-color="#d63072" stop-opacity="0.4"/>
          <stop offset="100%" stop-color="#e04a8a" stop-opacity="0"/>
        </radialGradient>
      </defs>
      <rect x="0" y="0" width="880" height="680" fill="url(#speakerWash)"/>
    </svg>

    <div class="slogan-band"></div>
    <p class="slogan">Music + Power</p>
  </main>
</body>
</html>
```